Stationery Design Project

We need, stationary designs for a store of children and juvenile furniture.
we have the logo. also need tags for the furniture with enought space to include description and options , maybe a 4" x 6" tag.

Target Market(s)

Parents of childrens and teens

Industry/Entity Type

Store

```html
<!DOCTYPE html>
<html lang="en">
<head>
<meta charset="utf-8">
<title>Birchnest – Presentation Folder</title>
<link href="https://fonts.googleapis.com/css2?family=Open+Sans:wght@400;600&display=swap" rel="stylesheet">
<style>
  :root {
    --teal: #54c4d0;
    --paper: #ffffff;
    --cloud-grey: #e6e7e8;
    --dieline: #a3302c;
    --accent-orange: #f07f2a;
    --text-grey: #7b7b7b;
    --brand-grey: #7a7a7a;
  }
  html, body {
    margin: 0;
    padding: 0;
    width: 1200px;
    height: 985px;
    overflow: hidden;
    background: var(--paper);
  }
  .folder-dieline {
    display: block;
    width: 1200px;
    height: 985px;
    font-family: "Open Sans", sans-serif;
  }
  .bleed-teal { fill: var(--teal); }
  .panel-white { fill: var(--paper); }
  .cut-line { fill: none; stroke: var(--dieline); stroke-width: 1; }
  .fold-line { fill: none; stroke: #3c4a55; stroke-width: 0.8; stroke-dasharray: 2 3; }
  .spine-fold { fill: none; stroke: var(--dieline); stroke-width: 0.8; stroke-dasharray: 2 3; }
  .cloud-decoration { fill: var(--cloud-grey); }
  .contact-icon { fill: var(--accent-orange); }
  .contact-glyph { fill: none; stroke: #fff; stroke-width: 1.2; stroke-linecap: round; stroke-linejoin: round; }
  .contact-text { fill: var(--text-grey); font-size: 7px; }
  .brand-name { fill: var(--brand-grey); font-size: 30px; font-weight: 600; letter-spacing: 1px; }
  .brand-dot { fill: var(--brand-grey); }
</style>
</head>
<body>
<svg class="folder-dieline" viewBox="0 0 1100 900" preserveAspectRatio="none" xmlns="http://www.w3.org/2000/svg">
  <rect class="bleed-teal" x="0" y="0" width="183" height="900"/>
  <rect class="bleed-teal" x="0" y="665" width="633" height="235"/>
  <rect class="panel-white" x="183" y="29" width="914" height="636"/>

  <rect class="cloud-decoration" role="img" aria-label="Soft grey cloud decoration across the inside spread"
        x="282" y="70" width="713" height="275" rx="120"/>

  <path class="cut-line" d="M183 29 H1097 V665 H633"/>

  <path class="cut-line" d="M183 29 H150 C112 30 86 62 83 105 L28 622 L172 665 H183"/>
  <line class="fold-line" x1="171" y1="32" x2="171" y2="662"/>
  <line class="fold-line" x1="183" y1="32" x2="183" y2="662"/>
  <line class="cut-line" x1="69" y1="524" x2="150" y2="580"/>

  <path class="cut-line" d="M183 665 L232 830 C242 858 262 870 280 871 C296 871 306 858 305 842 C304 826 290 815 272 813 L555 795 C585 792 605 772 612 745 L633 665"/>
  <line class="fold-line" x1="190" y1="675" x2="626" y2="675"/>
  <line class="cut-line" x1="258" y1="718" x2="289" y2="690"/>
  <line class="cut-line" x1="412" y1="781" x2="442" y2="753"/>

  <line class="spine-fold" x1="633" y1="32" x2="633" y2="662"/>
  <line class="spine-fold" x1="645" y1="32" x2="645" y2="662"/>

  <g class="contact-list">
    <g class="contact-item contact-address">
      <circle class="contact-icon" cx="222" cy="545" r="6.5"/>
      <path class="contact-glyph" d="M222 549 C219 545.5 219.5 542 222 541.5 C224.5 542 225 545.5 222 549 Z"/>
      <text class="contact-text" x="235" y="544.5">Office #, Building Street, City</text>
      <text class="contact-text" x="235" y="553.5">State XXXXX Country</text>
    </g>
    <g class="contact-item contact-phone">
      <circle class="contact-icon" cx="222" cy="567" r="6.5"/>
      <path class="contact-glyph" d="M219.5 564 L221 564 L221.5 566 L220.7 566.8 C221.3 568 222 568.7 223.2 569.3 L224 568.5 L226 569 V570.5 C222.5 571 219 567.5 219.5 564 Z"/>
      <text class="contact-text" x="235" y="569.5">123 456 7890</text>
    </g>
    <g class="contact-item contact-email">
      <circle class="contact-icon" cx="222" cy="587" r="6.5"/>
      <rect class="contact-glyph" x="218.5" y="584.5" width="7" height="5"/>
      <path class="contact-glyph" d="M218.5 584.5 L222 587.5 L225.5 584.5"/>
      <text class="contact-text" x="235" y="589.5">hello@birchnest.com</text>
    </g>
    <g class="contact-item contact-web">
      <circle class="contact-icon" cx="222" cy="607" r="6.5"/>
      <circle class="contact-glyph" cx="222" cy="607" r="3.5"/>
      <path class="contact-glyph" d="M218.5 607 H225.5 M222 603.5 C220.5 605.5 220.5 608.5 222 610.5 C223.5 608.5 223.5 605.5 222 603.5"/>
      <text class="contact-text" x="235" y="609.5">www.birchnest.com</text>
    </g>
  </g>

  <g class="brand-lockup">
    <circle class="brand-dot" cx="957" cy="566" r="8"/>
    <text class="brand-name" x="957" y="613" text-anchor="middle">Birchnest</text>
  </g>
</svg>
</body>
</html>
```